Brookvale Holdings Ltd - Logo and Business Card

Create a logo and business card design for our new company.

Canadian private investment company with holdings in Saskatchewan Oil and real-estate.

Target Market(s)

Investors

Industry/Entity Type

Finance

Contact Information for Business Card

Name - Dominic Harlow
Position - President
Phone - 306.482.7159
Website - www.brookvaleholdings.ca

Logo Text

Today. Tomorrow. Together. (Tag Line)

Colors

Designer to choose colors to be used in the design.

Requirements
Must have
• Logo Must Have - Type Font only
• Must be modern, professional and stand out from the crowd.
Nice to have
• Don't have any, blank slate.

```html
<!DOCTYPE html>
<html lang="en">
<head>
<meta charset="utf-8">
<title>Brookvale Holdings Ltd – Business Card</title>
<link href="https://fonts.googleapis.com/css2?family=Open+Sans:wght@400&family=Tinos:wght@700&display=swap" rel="stylesheet">
<style>
  :root {
    --stage: #c9c1b6;
    --card-light: #f1eeeb;
    --card-mid: #e0dbd6;
    --brand-red: #b8141c;
    --brand-red-dark: #8e0a10;
    --band-grey: #8a8a8a;
    --band-grey-light: #a9a9a9;
    --text-grey: #6b6b6b;
    --name-cream: #efe6da;
    --serif: "Tinos", "Times New Roman", serif;
    --sans: "Open Sans", Arial, sans-serif;
  }
  html, body {
    margin: 0;
    padding: 0;
    width: 1200px;
    height: 970px;
    overflow: hidden;
    background: var(--stage);
  }
  .canvas {
    position: relative;
    width: 1200px;
    height: 970px;
  }
  .business-card {
    position: absolute;
    left: 80px;
    top: 190px;
    width: 1040px;
    height: 592px;
    box-shadow: 0 14px 40px rgba(0,0,0,0.25);
  }
  .business-card svg { display: block; width: 100%; height: 100%; }
  .holder-name { font-family: var(--serif); font-weight: 700; font-size: 38px; fill: var(--name-cream); }
  .holder-title { font-family: var(--sans); font-size: 26px; fill: var(--name-cream); }
  .company-name { font-family: var(--serif); font-weight: 700; font-size: 37px; fill: var(--text-grey); }
  .contact-text { font-family: var(--sans); font-size: 25px; fill: var(--text-grey); }
  .contact-icon-bg { fill: var(--brand-red); }
  .contact-icon { fill: none; stroke: #fff; stroke-width: 2; }
  .brand-word { font-family: var(--sans); font-weight: 400; font-size: 30px; fill: var(--text-grey); }
  .brand-tagline { font-family: var(--sans); font-weight: 400; font-size: 18px; fill: var(--text-grey); }
  .brand-dot { fill: var(--brand-red); }
</style>
</head>
<body>
<main class="canvas">
  <section class="business-card" aria-label="Business card for Brookvale Holdings Ltd">
    <svg viewBox="0 0 1040 592" xmlns="http://www.w3.org/2000/svg">
      <defs>
        <linearGradient id="card-surface" x1="0" y1="0" x2="1" y2="1">
          <stop offset="0" stop-color="var(--card-light)"/>
          <stop offset="1" stop-color="var(--card-mid)"/>
        </linearGradient>
        <linearGradient id="red-band" x1="0" y1="1" x2="1" y2="0">
          <stop offset="0" stop-color="var(--brand-red)"/>
          <stop offset="0.5" stop-color="var(--brand-red-dark)"/>
          <stop offset="1" stop-color="var(--brand-red)"/>
        </linearGradient>
      </defs>

      <rect class="card-surface" width="1040" height="592" fill="url(#card-surface)" stroke="#b9b3ad"/>

      <polygon class="grey-band" points="0,240 732,58 1040,195 1040,262 732,66 0,282" fill="var(--band-grey)"/>
      <polygon class="red-band" points="0,0 1040,0 1040,195 732,58 0,240" fill="url(#red-band)"/>
      <polygon class="band-edge" points="0,240 732,58 1040,195 1040,200 732,64 0,246" fill="var(--band-grey-light)"/>

      <text class="holder-name" x="50" y="100">Dominic Harlow</text>
      <text class="holder-title" x="50" y="131">President</text>

      <text class="company-name" x="48" y="395">Brookvale Holdings Ltd</text>

      <rect class="contact-icon-bg" x="50" y="440" width="32" height="32"/>
      <path class="contact-icon" d="M56 452 q10 -8 20 0 l-3 4 h-3 l-1 -3 h-6 l-1 3 h-3 z M58 458 h16 v9 h-16 z"/>
      <text class="contact-text" x="97" y="465">306.482.7159</text>

      <rect class="contact-icon-bg" x="50" y="479" width="32" height="32"/>
      <path class="contact-icon" d="M56 487 h20 v16 h-20 z M56 487 l10 9 l10 -9 M56 503 l7 -7 M76 503 l-7 -7"/>
      <text class="contact-text" x="97" y="503">info@brookvaleholdings.ca</text>

      <rect class="contact-icon-bg" x="50" y="518" width="32" height="32"/>
      <g class="contact-icon">
        <circle cx="66" cy="534" r="10"/>
        <ellipse cx="66" cy="534" rx="4.5" ry="10"/>
        <path d="M56 534 h20 M58 528 h16 M58 540 h16"/>
      </g>
      <text class="contact-text" x="97" y="542">www.brookvaleholdings.ca</text>

      <circle class="brand-dot" cx="812" cy="390" r="38"/>
      <text class="brand-word" x="812" y="508" text-anchor="middle">Brookvale Holdings Ltd</text>
      <text class="brand-tagline" x="812" y="542" text-anchor="middle">Today. Tomorrow. Together.</text>
    </svg>
  </section>
</main>
</body>
</html>
```